Spiritual Self Help Book Cover

I need a book cover that's extremely appealing to spiritual seekers, self-help/health and wellness fans. Mostly for women.
The book blends spirituality/mysticism with science for readers to understand how to optimize their health/body, emotional well-being, mental wellness, spiritual fulfillment, relationships, business and purpose in life. It infuses ancient and modern understanding of energy/frequency/quantum mechanics along with the science of chiropractic and psychology.
Book title: Folding Every Lantern Inward
I'll attach some examples that are similar to what I like but I want something different and more extravagantly beautiful.
Please use the graphic of the Sri Yantra Mandala into the cover instead of this stock image one.
I'll need the book cover in all formats: paperback, hardcover, ebook and audiobook.
I'll provide the rest of the details, including publisher logo, synopsis, author photo/blurb and ISBN after I pick the final wniner.
Mostly women spiritual seekers, self-help readers, health/wellness enthusiasts

```html
<!DOCTYPE html>
<html lang="en">
<head>
<meta charset="utf-8">
<title>Folding Every Lantern Inward — Book Cover</title>
<link href="https://fonts.googleapis.com/css2?family=Arimo:wght@700&family=Michroma&display=swap" rel="stylesheet">
<style>
  :root {
    --blush: #f8d6e4;
    --sky-pink: #f4b6cc;
    --rose: #ef9fb6;
    --lilac: #b9a5d2;
    --periwinkle: #8f9dd0;
    --sky-blue: #8cb8e2;
    --mandala-coral: #ee8f9f;
    --mandala-pink: #f2a7bb;
    --mandala-mauve: #8f77b4;
    --ring-light: rgba(255, 235, 240, 0.55);
    --disc-light: rgba(255, 220, 228, 0.45);
    --speck: rgba(255, 255, 255, 0.85);
    --title-white: #ffffff;
    --title-shadow: rgba(110, 50, 80, 0.45);
  }
  html, body {
    margin: 0;
    padding: 0;
    width: 804px;
    height: 1200px;
    overflow: hidden;
  }
  .cover {
    position: relative;
    width: 804px;
    height: 1200px;
    overflow: hidden;
    background:
      radial-gradient(ellipse 45% 25% at 10% 25%, rgba(250, 225, 236, 0.85), transparent 70%),
      radial-gradient(ellipse 45% 25% at 92% 12%, rgba(242, 165, 196, 0.7), transparent 70%),
      radial-gradient(ellipse 40% 20% at 5% 75%, rgba(160, 200, 235, 0.7), transparent 70%),
      linear-gradient(180deg, var(--blush) 0%, var(--sky-pink) 20%, var(--rose) 40%, var(--lilac) 64%, var(--periwinkle) 82%, var(--sky-blue) 100%);
  }
  .mandala {
    position: absolute;
    left: 0;
    top: 0;
    width: 804px;
    height: 1200px;
  }
  .title {
    margin: 0;
    font-family: "Arimo", Arial, sans-serif;
    font-weight: 700;
    color: var(--title-white);
    text-transform: uppercase;
  }
  .title-line {
    position: absolute;
    left: 0;
    width: 804px;
    text-align: center;
    line-height: 1;
    white-space: nowrap;
    text-shadow: 3px 4px 4px var(--title-shadow);
  }
  .line-one   { top: 309px; font-size: 98px;  letter-spacing: 6px; }
  .line-two   { top: 439px; font-size: 132px; }
  .line-three { top: 590px; font-size: 104px; letter-spacing: 2px; }
  .line-four  { top: 718px; font-size: 136px; }
  .author {
    position: absolute;
    left: 0;
    top: 1080px;
    width: 804px;
    margin: 0;
    text-align: center;
    font-family: "Michroma", Arial, sans-serif;
    font-size: 24px;
    line-height: 1;
    letter-spacing: 5px;
    color: var(--title-white);
    text-transform: uppercase;
  }
</style>
</head>
<body>
  <main class="cover">
    <svg class="mandala" viewBox="0 0 804 1200" role="img" aria-label="Sri Yantra lotus mandala with interlocking triangles and petals in soft coral and mauve, centred behind the title">
      <defs>
        <radialGradient id="lotusHalo" cx="50%" cy="50%" r="50%">
          <stop offset="0%" stop-color="var(--mandala-coral)" stop-opacity="0.55"/>
          <stop offset="80%" stop-color="var(--mandala-coral)" stop-opacity="0.45"/>
          <stop offset="100%" stop-color="var(--mandala-coral)" stop-opacity="0"/>
        </radialGradient>
        <linearGradient id="lotusTone" x1="0" y1="0" x2="0" y2="1">
          <stop offset="0%" stop-color="var(--mandala-coral)" stop-opacity="0.6"/>
          <stop offset="55%" stop-color="var(--mandala-pink)" stop-opacity="0.45"/>
          <stop offset="100%" stop-color="var(--mandala-mauve)" stop-opacity="0.55"/>
        </linearGradient>
        <radialGradient id="innerGlow" cx="50%" cy="45%" r="50%">
          <stop offset="0%" stop-color="#f6c3c8" stop-opacity="0.7"/>
          <stop offset="100%" stop-color="#e9a2b8" stop-opacity="0.35"/>
        </radialGradient>
        <radialGradient id="topLotus" cx="50%" cy="0%" r="60%">
          <stop offset="0%" stop-color="var(--mandala-pink)" stop-opacity="0.5"/>
          <stop offset="100%" stop-color="var(--mandala-pink)" stop-opacity="0"/>
        </radialGradient>
      </defs>

      <ellipse class="upper-lotus" cx="403" cy="20" rx="240" ry="110" fill="url(#topLotus)"/>

      <circle class="lotus-halo" cx="403" cy="600" r="470" fill="url(#lotusHalo)"/>
      <circle class="lotus-body" cx="403" cy="600" r="420" fill="url(#lotusTone)"/>
      <circle class="outer-ring" cx="403" cy="600" r="368" fill="none" stroke="var(--ring-light)" stroke-width="10"/>
      <circle class="inner-disc" cx="403" cy="600" r="278" fill="url(#innerGlow)"/>
      <circle class="inner-ring" cx="403" cy="600" r="278" fill="none" stroke="var(--disc-light)" stroke-width="4"/>
      <circle class="bindu" cx="403" cy="598" r="7" fill="#e98a9a" fill-opacity="0.7"/>

      <g class="specks" fill="var(--speck)">
        <circle cx="75" cy="108" r="3"/><circle cx="108" cy="72" r="2"/>
        <circle cx="82" cy="165" r="2.5"/><circle cx="360" cy="126" r="2"/>
        <circle cx="690" cy="282" r="2.5"/><circle cx="752" cy="470" r="2"/>
        <circle cx="700" cy="672" r="2.5"/><circle cx="152" cy="888" r="3"/>
        <circle cx="50" cy="312" r="2"/><circle cx="620" cy="980" r="2"/>
        <circle cx="205" cy="1135" r="3"/><circle cx="745" cy="1008" r="2"/>
        <circle cx="30" cy="410" r="2"/><circle cx="560" cy="90" r="2"/>
      </g>
    </svg>

    <h1 class="title">
      <span class="title-line line-one">Folding</span>
      <span class="title-line line-two">Every</span>
      <span class="title-line line-three">Lantern</span>
      <span class="title-line line-four">Inward</span>
    </h1>

    <p class="author">Dr. Mira Holloway</p>
  </main>
</body>
</html>
```